Literary novel entitled 'Lanternfall Rust'

Paper back dimensions approx 8 in x 5.25 in x 1 in (350 words about)
For the design of the front cover, I was picturing faces/heads coloured blue, wearing dark glasses. Faces could be 'real' or stylized, probably without expression. These are two protagonists so probably two faces but would consider more e.g. overlapping images of the two, or it can be images either facing one another, looking forward or somewhere between.
A piano keyboard, or part of one, in which white keys are blue. Keyboard not necessarily linear.
Some scrolling at foot of cover (to denote the sea) going onto spine and back cover.
At top of back cover an image (probably photographic) of St Odrel basilica, Venice with some foreground of St Odrel square. The base of the building is blue, the middle, red and top, green in the manner of a 'Velmaine'.
wide readership

```html
<!DOCTYPE html>
<html lang="en">
<head>
<meta charset="utf-8">
<title>Lanternfall Rust — Front Cover</title>
<link rel="stylesheet" href="https://fonts.googleapis.com/css2?family=Oswald:wght@200;300&display=swap">
<style>
  :root {
    --page-bg: #eef1f3;
    --cover-bg: #ffffff;
    --cover-edge: #2b2b2b;
    --author-ink: #0e6f86;
    --water-light: #7fd3e6;
    --water-mid: #3aa6cf;
    --water-deep: #1679b2;
    --water-glow: #bfe9ef;
  }
  * { margin: 0; padding: 0; box-sizing: border-box; }
  html, body {
    width: 1200px;
    height: 800px;
    overflow: hidden;
    background: var(--page-bg);
  }
  .stage {
    width: 1200px;
    height: 800px;
    display: flex;
    align-items: center;
    justify-content: center;
  }
  .cover {
    width: 480px;
    height: 740px;
    background: var(--cover-bg);
    border: 1px solid var(--cover-edge);
    display: block;
  }
  .author-name {
    font-family: "Oswald", sans-serif;
    font-weight: 300;
    fill: var(--author-ink);
  }
  .title-line {
    font-family: "Oswald", sans-serif;
    font-weight: 300;
  }
</style>
</head>
<body>
  <main class="stage">
    <svg class="cover" viewBox="0 0 480 740" xmlns="http://www.w3.org/2000/svg" aria-label="Front cover of Lanternfall Rust">
      <defs>
        <linearGradient id="water-type" x1="0" y1="0" x2="0" y2="1">
          <stop offset="0" stop-color="var(--water-light)"/>
          <stop offset="0.5" stop-color="var(--water-mid)"/>
          <stop offset="1" stop-color="var(--water-deep)"/>
        </linearGradient>
        <radialGradient id="water-keys" cx="0.45" cy="0.35" r="0.8">
          <stop offset="0" stop-color="var(--water-glow)"/>
          <stop offset="0.35" stop-color="var(--water-mid)"/>
          <stop offset="1" stop-color="var(--water-deep)"/>
        </radialGradient>
      </defs>

      <text class="author-name" x="240" y="138" text-anchor="middle" font-size="28">AUTHOR NAME</text>

      <g class="title" fill="url(#water-type)">
        <text class="title-line title-line--upper" x="9" y="351" font-size="80" textLength="463" lengthAdjust="spacingAndGlyphs">LANTERNFALL</text>
        <text class="title-line title-line--lower" x="9" y="516" font-size="190" textLength="463" lengthAdjust="spacingAndGlyphs">RUST</text>
      </g>

      <rect class="keyboard-rail" x="6" y="519" width="468" height="4" fill="var(--water-deep)"/>

      <rect class="keyboard" x="9" y="525" width="463" height="208" fill="url(#water-keys)"
            role="img" aria-label="Piano keyboard whose keys are filled with rippling blue sea water"/>
    </svg>
  </main>
</body>
</html>
```